Hawaiian skin care product needs label design

We are looking for a font for Hawaiian skin care product called 'umo - which means 'skin' in Hawaiian.
No need for a logo or a mark, simply looking for a clean, fresh, modern, young, and crisp font and background for our product label.
We are creating the label for the product bag, see file attached for reference.
Ideas we like: Subtle gradient water color back ground, fade chevron, see files attached.
This is a women's product, but don't want it to be too feminine or overly girly. Fresh and crisp, modern with subtle undertones of femininity.
Updates

Reason: Need to have the back of the label created as well.

Target Market(s)

Women, ages 18-40 Up scale, modern, hip. Mature and sophisticated.

Industry/Entity Type

Skin Care Product

Logo Text

'umo

Logo styles of interest
Wordmark Logo
Font styles to use
Sans Serif

Requirements
Must have
• This is for a label on a bag, attached images below to show our bag, pouch. We are not sure which color to go with as of yet.
Should not have
• No logo, no need for a mark of any kind.
Not childish or overly girly.

```html
<!DOCTYPE html>
<html lang="en">
<head>
<meta charset="UTF-8">
<title>'umo Label</title>
<link rel="stylesheet" href="https://fonts.googleapis.com/css2?family=Oswald:wght@500&display=swap">
<style>
  :root {
    --canvas-bg: #e8ecf0;
    --label-white: #ffffff;
    --brand-blue: #1c9cc6;
    --tone-coral: #f7a8a0;
    --tone-peach: #f9c9a4;
    --tone-lemon: #f6e7a2;
    --tone-sky: #a9dcef;
    --tone-aqua: #8fd3ea;
  }
  * { margin: 0; padding: 0; box-sizing: border-box; }
  html, body {
    width: 1200px;
    height: 1000px;
    overflow: hidden;
    background: var(--canvas-bg);
  }
  .canvas {
    position: relative;
    width: 1200px;
    height: 1000px;
  }
  .label {
    position: absolute;
    left: 100px;
    top: 298px;
    width: 1000px;
    height: 404px;
    background: var(--label-white);
    overflow: hidden;
    box-shadow: 0 2px 10px rgba(60, 70, 80, 0.15);
  }
  .chevron-field {
    position: absolute;
    top: 0;
    height: 100%;
    width: 44%;
    background: linear-gradient(180deg,
      var(--tone-sky) 0%, var(--tone-lemon) 18%, var(--tone-coral) 34%,
      var(--tone-aqua) 50%, var(--tone-peach) 66%, var(--tone-sky) 82%,
      var(--tone-coral) 100%);
  }
  .chevron-field--left {
    left: 0;
    -webkit-mask-image: linear-gradient(90deg, #000 0%, rgba(0,0,0,0.75) 45%, transparent 100%);
    mask-image: linear-gradient(90deg, #000 0%, rgba(0,0,0,0.75) 45%, transparent 100%);
  }
  .chevron-field--right {
    right: 0;
    -webkit-mask-image: linear-gradient(270deg, #000 0%, rgba(0,0,0,0.75) 45%, transparent 100%);
    mask-image: linear-gradient(270deg, #000 0%, rgba(0,0,0,0.75) 45%, transparent 100%);
  }
  .wordmark {
    position: absolute;
    left: 0;
    right: 0;
    top: 50%;
    transform: translateY(-50%);
    text-align: center;
    font-family: "Oswald", "Arial Narrow", sans-serif;
    font-weight: 500;
    font-size: 150px;
    line-height: 1;
    color: var(--brand-blue);
    letter-spacing: 2px;
  }
</style>
</head>
<body>
  <main class="canvas">
    <section class="label">
      <div class="chevron-field chevron-field--left" role="img" aria-label="Pastel watercolor chevron pattern in coral, yellow and sky blue fading toward the center"></div>
      <div class="chevron-field chevron-field--right" role="img" aria-label="Pastel watercolor chevron pattern in coral, yellow and sky blue fading toward the center"></div>
      <h1 class="wordmark">'umo</h1>
    </section>
  </main>
</body>
</html>
```